Private chef located in Vail, CO

I would like my info located at the top of the landing page, perhaps some Vail mountain landscapes that I could swap out from summer to winter photos. I need the menu bar to have a link to a blog, about me, photo gallery, recipes & beer reviews. I would also like to have a shop, but only populated with products from quolex or other online retailers that I can affiliate with.
Target Market(s)
Extremely wealthy, affluent people, concierge, international
Number of Pages Required
5+ page

```html
<!DOCTYPE html>
<html lang="en">
<head>
<meta charset="utf-8">
<title>Private Chef</title>
<link href="https://fonts.googleapis.com/css2?family=Open+Sans:wght@400;600;700&family=Source+Sans+3:wght@400;600;700&display=swap" rel="stylesheet">
<style>
:root{
  --violet:#8d7fc0;
  --violet-deep:#5b5d9e;
  --slate:#6e7fab;
  --coral:#e55a3f;
  --paper:#eef0f5;
  --card:#f2f3f7;
  --ink:#2c2c34;
  --white:#ffffff;
}
*{margin:0;padding:0;box-sizing:border-box}
html,body{width:1200px;height:2394px;overflow:hidden}
body{position:relative;background:var(--paper);font-family:"Source Sans 3",sans-serif;color:var(--ink)}
.abs{position:absolute}

/* hero */
.hero{left:0;top:0;width:1200px;height:726px;
  background:linear-gradient(180deg,#a77fc7 0%,#9b86c9 22%,#8f8bc8 40%,#b0a4d6 55%,#6b73aa 75%,#3f4c82 100%)}
.nav a{position:absolute;top:50px;color:var(--white);font-weight:600;font-size:17px;text-decoration:none;white-space:nowrap}
.nav .star{position:absolute;top:50px;color:var(--white);font-size:14px}
.brand{position:absolute;left:540px;top:44px;width:120px;text-align:center;color:var(--white);font-weight:700;font-size:19px;line-height:1.1}
.hero-title{left:146px;top:208px;font-family:"Open Sans",sans-serif;font-weight:600;font-size:92px;color:var(--white);letter-spacing:2px;line-height:1}
.hero-text{left:153px;top:334px;width:650px;font-size:24px;line-height:36px;color:var(--white)}
.hero-rule{left:153px;top:469px;width:710px;height:2px;background:rgba(255,255,255,.8)}
.btn-outline{left:153px;top:501px;width:165px;height:42px;border:2px solid var(--white);color:var(--white);font-weight:700;font-size:14px;display:flex;align-items:center;justify-content:center;gap:7px}

/* signup */
.signup{left:239px;top:665px;width:723px;height:119px;display:flex;box-shadow:0 6px 18px rgba(40,40,80,.15)}
.signup-intro{width:361px;background:var(--white);border-left:5px solid var(--coral);text-align:center;padding-top:20px}
.ornament{display:block;margin:0 auto 6px;width:140px;height:30px;border-radius:15px;background:linear-gradient(90deg,transparent,#b7bcd6,transparent)}
.signup-intro h3{font-size:17px;font-weight:700;color:var(--slate);letter-spacing:.5px}
.signup-intro p{font-size:11px;color:#7a7f95;margin-top:4px}
.signup-form{width:314px;background:var(--slate);padding:22px 0 0 50px;color:var(--white)}
.signup-form label{font-size:12px;font-weight:700;display:block;margin-bottom:8px}
.email{width:213px;height:40px;background:var(--white);display:flex;align-items:center;gap:10px;padding-left:14px;font-size:12px;color:var(--slate)}
.signup-go{width:48px;background:var(--coral);display:flex;align-items:center;justify-content:center}

/* story */
.story{left:99px;top:867px;width:996px;height:466px;background:var(--card);box-shadow:0 10px 26px rgba(60,60,100,.18)}
.story h2{position:absolute;left:0;top:54px;width:613px;text-align:center;font-weight:400;font-size:42px;color:var(--ink)}
.story-mark{position:absolute;left:186px;top:120px;width:240px;height:1px;background:#c9ccd8}
.story-mark span{position:absolute;left:50%;top:-9px;transform:translateX(-50%);background:var(--card);padding:0 8px;font-weight:700;font-size:13px;color:var(--ink);white-space:nowrap}
.story-lead{position:absolute;left:60px;top:152px;width:494px;text-align:center;font-size:15px;font-weight:700;line-height:22px}
.story-rule{position:absolute;left:55px;top:238px;width:503px;height:1px;background:#d8dae3}
.story-body{position:absolute;left:60px;top:258px;width:494px;text-align:center;font-size:15px;line-height:22px}
.story-photo{position:absolute;left:613px;top:0;width:361px;height:466px;background:linear-gradient(180deg,#a796cc 0%,#7f76ad 45%,#4c5585 100%)}
.dots{position:absolute;left:982px;top:194px;display:flex;flex-direction:column;gap:7px}
.dots i{width:7px;height:7px;border-radius:50%;background:var(--slate);display:block}
.dots i.on{background:var(--coral)}

/* shop */
.shop{left:0;top:1424px;width:1200px;height:970px;background:linear-gradient(180deg,#8c82c2 0%,#8179b6 40%,#6f72aa 70%,#6b78ad 100%)}
.frame{left:204px;top:1518px;width:895px;height:768px;border-top:2px solid rgba(255,255,255,.8);border-right:2px solid rgba(255,255,255,.8)}
.shop-title{left:99px;top:1560px;font-family:"Open Sans",sans-serif;font-weight:700;font-size:78px;color:var(--white);line-height:1}
.shop-sub{left:99px;top:1634px;font-size:15px;color:var(--white)}
.shop-text{left:99px;top:1679px;width:400px;font-size:15px;line-height:22px;color:var(--white)}
.products{left:584px;top:1534px;width:498px;height:756px;box-shadow:0 10px 28px rgba(30,30,70,.25)}
.product-list{background:var(--white);height:600px;padding:21px 35px 0 35px}
.product{display:flex;gap:25px;height:201px;border-bottom:1px solid #e3e4ea}
.product:last-child{border-bottom:none}
.product-photo{width:198px;height:155px;flex:none}
.product h4{font-weight:400;font-size:21px;margin-top:12px;color:var(--ink)}
.price{color:var(--coral);font-weight:600;font-size:19px;margin:6px 0 5px 4px}
.product p{font-size:12px;line-height:17px;width:196px}
.btn-shop{margin-top:10px;width:88px;height:32px;background:var(--coral);color:var(--white);font-weight:700;font-size:13px;display:flex;align-items:center;justify-content:center;gap:6px}
.shop-foot{height:156px;background:var(--coral);text-align:center;color:var(--white);padding-top:34px;position:relative}
.foot-ornament{position:absolute;left:44px;top:22px;width:410px;height:70px;border-radius:35px;background:radial-gradient(ellipse at center,rgba(200,70,45,.6),rgba(229,90,63,0) 70%)}
.foot-brand{position:relative;font-weight:700;font-size:20px}
.shop-foot p{position:relative;margin-top:14px;font-size:20px}
</style>
</head>
<body>

<section class="abs hero" role="img" aria-label="Snow-covered mountain range under a violet sunset sky"></section>

<nav class="nav">
  <a style="left:204px">about me</a>
  <span class="star" style="left:322px">★</span>
  <a style="left:367px">blog update</a>
  <span class="star" style="left:487px">★</span>
  <div class="brand">Private<br>Chef</div>
  <span class="star" style="left:698px">★</span>
  <a style="left:733px">photo gallery</a>
  <span class="star" style="left:878px">★</span>
  <a style="left:925px">recipes &amp; beer reviews</a>
</nav>

<h1 class="abs hero-title">Private chef</h1>
<p class="abs hero-text">Lorem ipsum dolor sit amet, consectetur adipiscing elit, sed<br>do eiusmod tempor incididunt ut labore et dolore magna<br>aliqua. Ut enim ad minim veniam.</p>
<div class="abs hero-rule"></div>
<div class="abs btn-outline">READ MORE
  <svg width="13" height="13" viewBox="0 0 13 13"><circle cx="6.5" cy="6.5" r="6.5" fill="#fff"/><path d="M5 3.5l3 3-3 3" stroke="#8d7fc0" stroke-width="1.6" fill="none"/></svg>
</div>

<section class="abs signup">
  <div class="signup-intro">
    <span class="ornament" role="img" aria-label="Decorative flourish"></span>
    <h3>NEVER MISS A THING</h3>
    <p>Receive latest blog posts, news and weekly inspirations</p>
  </div>
  <div class="signup-form">
    <label>SIGN UP</label>
    <div class="email">
      <svg width="15" height="11" viewBox="0 0 15 11"><rect x=".5" y=".5" width="14" height="10" fill="none" stroke="#9aa3c2"/><path d="M.5 .5l7 5 7-5" fill="none" stroke="#9aa3c2"/></svg>
      your email address
    </div>
  </div>
  <div class="signup-go">
    <svg width="14" height="22" viewBox="0 0 14 22"><path d="M3 3l8 8-8 8" stroke="#fff" stroke-width="2" fill="none"/></svg>
  </div>
</section>

<article class="abs story">
  <h2>My Story</h2>
  <div class="story-mark"><span>Private Chef</span></div>
  <p class="story-lead">Lorem ipsum dolor sit amet, consectetur adipiscing elit, sed do eiusmod tempor incididunt ut labore et dolore magna aliqua. Ut enim ad minim veniam, quis nostrud exercitation ullamco laboris nisi ut</p>
  <div class="story-rule"></div>
  <p class="story-body">Lorem ipsum dolor sit amet, consectetur adipiscing elit, sed do eiusmod tempor incididunt ut labore et dolore magna aliqua. Ut enim ad minim veniam, quis nostrud exercitation ullamco laboris nisi ut aliquip ex ea commodo consequat. Duis aute irure dolor in reprehenderit in voluptate velit esse cillum dolore eu fugiat nulla pariatur. Excepteur sint occaecat cupidatat non proident, sunt in culpa qui officia</p>
  <div class="story-photo" role="img" aria-label="Photographer in a beanie and jacket holding a camera in misty mountains"></div>
  <div class="dots"><i></i><i class="on"></i><i></i><i></i><i></i></div>
</article>

<section class="abs shop" role="img" aria-label="Mountain lake with autumn forest in a violet haze"></section>
<div class="abs frame"></div>
<h2 class="abs shop-title">SHOP</h2>
<p class="abs shop-sub">Private chef products</p>
<p class="abs shop-text">Lorem ipsum dolor sit amet, consectetur adipiscing elit, sed<br>do eiusmod tempor incididunt ut labore et dolore magna<br>aliqua. Ut enim ad minim veniam.</p>

<section class="abs products">
  <div class="product-list">
    <div class="product">
      <div class="product-photo" role="img" aria-label="Two orange cocktails with lime on a dark board" style="background:linear-gradient(135deg,#3a3530,#e8763a 55%,#6a4a30)"></div>
      <div>
        <h4>Consectetur adipisc</h4>
        <div class="price">$ 450</div>
        <p>Lorem ipsum dolor sit amet, conssa<br>tetur adipiscing elit,sed do.</p>
        <div class="btn-shop">SHOP <svg width="11" height="11" viewBox="0 0 11 11"><circle cx="5.5" cy="5.5" r="5.5" fill="#fff"/><path d="M4.3 3l2.5 2.5-2.5 2.5" stroke="#e55a3f" stroke-width="1.4" fill="none"/></svg></div>
      </div>
    </div>
    <div class="product">
      <div class="product-photo" role="img" aria-label="Plate of roasted chicken with herbs" style="background:linear-gradient(135deg,#e0a13a,#a8541f 55%,#3d5f6e)"></div>
      <div>
        <h4>Lonsectetur lodipisc</h4>
        <div class="price">$ 450</div>
        <p>Lorem ipsum dolor sit amet, conssa<br>tetur adipiscing elit,sed do.</p>
        <div class="btn-shop">SHOP <svg width="11" height="11" viewBox="0 0 11 11"><circle cx="5.5" cy="5.5" r="5.5" fill="#fff"/><path d="M4.3 3l2.5 2.5-2.5 2.5" stroke="#e55a3f" stroke-width="1.4" fill="none"/></svg></div>
      </div>
    </div>
    <div class="product">
      <div class="product-photo" role="img" aria-label="Camera on a wooden table" style="background:linear-gradient(135deg,#3b2e26,#5a4437 55%,#2a2624)"></div>
      <div>
        <h4>Qaectetur adaipisc</h4>
        <div class="price">$ 450</div>
        <p>Lorem ipsum dolor sit amet, conssa<br>tetur adipiscing elit,sed do.</p>
        <div class="btn-shop">SHOP <svg width="11" height="11" viewBox="0 0 11 11"><circle cx="5.5" cy="5.5" r="5.5" fill="#fff"/><path d="M4.3 3l2.5 2.5-2.5 2.5" stroke="#e55a3f" stroke-width="1.4" fill="none"/></svg></div>
      </div>
    </div>
  </div>
  <footer class="shop-foot">
    <div class="foot-ornament" role="img" aria-label="Faint decorative flourish"></div>
    <div class="foot-brand">Private Chef</div>
    <p>Copyright © 2019 Private Chef.</p>
  </footer>
</section>

</body>
</html>
```